hello! I need a very simple modern business card for a new venture called The Quiet Harbor Retreats. It's the very first Tech-Free retreat in Asia!

The concept is very unique. Basically a group of 12-15 people would go on a 3 to 4 days retreat where no phone or internet is allowed. The first retreat will take place in a beautiful villa in Bali by the sea. It will include yoga, meditation, art & writing workshops, swimming, hiking, cooking, healthy vegetarian meals, etc.

Reason: Thanks for your submissions. I still haven't found exactly what I'm after but the designs that haven't be eliminated are getting close.. Please keep in mind that it should be a simple, modern and upmarket business card. Thanks

Target Market(s)

Both men and women who would like to disconnect from life, computer and phone for 3/4 days. They can be either local or expats but based in Asia (Singapore, Hong Kong).
Client will have to pay for their own flight and then the price is around US$600 for a 3-day retreat including everything (accommodation, food, activities). It means clients already have a good income. They are usually working in marketing, advertising, digital media, public relations.

Industry/Entity Type

Internet

Font styles to use
Other font styles liked:
• anything modern you like

Colors
acd036
9bcb3c
f37022
f68d4d
1b1b1b
333333
acd037

Requirements
Must have
• Name: Lina Vorel
Position: #gadgetdevotee
Company: The Quiet Harbor Retreats (asia should be smaller than the rest)
- Email button - quietharborretreats@mailverra.com
- FriendSpace button - www.friendspace.com/quietharborretreats
- TicketNest button - www.quietharborretreats.ticketnest.com
Nice to have
• You can use my logo attached but it's something I designed quickly on Power Point so it would be nice to include your own version.
Should not have
• anything tacky or girly or childish. thanks

```html
<!DOCTYPE html>
<html lang="en">
<head>
<meta charset="utf-8">
<title>The Quiet Harbor Retreats – Business Card</title>
<link rel="stylesheet" href="https://fonts.googleapis.com/css2?family=Della+Respira&family=Nunito+Sans:wght@400&display=swap">
<style>
  :root {
    --paper: #ffffff;
    --leaf-green: #b5d775;
    --leaf-green-deep: #9bcb3c;
    --leaf-green-soft: #c6e08f;
    --band-amber: #e2a63f;
    --harbor-orange: #f6901e;
    --icon-glow: #f8ab5c;
    --ink: #1b1b1b;
    --ink-soft: #333333;
    --white: #ffffff;
  }
  * { margin: 0; padding: 0; box-sizing: border-box; }
  html, body {
    width: 804px;
    height: 1200px;
    overflow: hidden;
    background: var(--paper);
  }
  .sheet {
    position: relative;
    width: 804px;
    height: 1200px;
  }

  /* Front side */
  .card-front {
    position: absolute;
    left: 27px;
    top: 43px;
    width: 742px;
    height: 426px;
    border: 2px solid var(--ink);
    overflow: hidden;
  }
  .card-front__foliage {
    position: absolute;
    inset: 0;
    background:
      radial-gradient(ellipse at 15% 40%, var(--leaf-green-soft) 0%, transparent 45%),
      radial-gradient(ellipse at 90% 85%, var(--leaf-green-deep) 0%, transparent 40%),
      var(--leaf-green);
  }
  .company {
    position: absolute;
    left: 0;
    top: 0;
    width: 100%;
  }
  .company__name {
    position: absolute;
    right: 40px;
    top: 38px;
    font-family: "Della Respira", serif;
    font-size: 62px;
    line-height: 1;
    color: var(--ink);
    white-space: nowrap;
    z-index: 2;
  }
  .company__band {
    position: absolute;
    left: -2px;
    top: 108px;
    width: 702px;
    height: 53px;
    background: var(--band-amber);
    opacity: 0.92;
  }
  .company__region {
    position: absolute;
    right: 9px;
    top: 8px;
    font-family: "Della Respira", serif;
    font-size: 34px;
    line-height: 1;
    letter-spacing: 1px;
    color: var(--white);
  }
  .person__band {
    position: absolute;
    left: 44px;
    top: 279px;
    width: 700px;
    height: 52px;
    background: var(--band-amber);
    opacity: 0.92;
  }
  .person__name {
    position: absolute;
    left: 10px;
    top: 7px;
    font-family: "Della Respira", serif;
    font-size: 38px;
    line-height: 1;
    color: var(--white);
  }
  .person__role {
    position: absolute;
    left: 54px;
    top: 336px;
    font-family: "Nunito Sans", sans-serif;
    font-size: 27px;
    line-height: 1;
    color: var(--ink-soft);
  }

  /* Back side */
  .card-back {
    position: absolute;
    left: 39px;
    top: 733px;
    width: 741px;
    height: 423px;
    background: var(--harbor-orange);
    overflow: hidden;
  }
  .card-back__power {
    position: absolute;
    left: 0;
    top: 0;
  }
  .contact {
    position: absolute;
    left: 0;
    top: 190px;
    width: 100%;
    list-style: none;
    text-align: center;
    font-family: "Nunito Sans", sans-serif;
    font-size: 22px;
    line-height: 34.5px;
    color: var(--white);
  }
</style>
</head>
<body>
<main class="sheet">

  <section class="card-front" aria-label="Business card front">
    <div class="card-front__foliage" role="img" aria-label="Soft green bamboo leaves background"></div>

    <div class="company">
      <h1 class="company__name">The Quiet Harbor</h1>
      <div class="company__band">
        <span class="company__region">RETREATS</span>
      </div>
    </div>

    <div class="person__band">
      <h2 class="person__name">Lina Vorel</h2>
    </div>
    <p class="person__role">Gadgetdevotee</p>
  </section>

  <section class="card-back" aria-label="Business card back">
    <svg class="card-back__power" width="741" height="423" viewBox="0 0 741 423" aria-hidden="true">
      <path d="M 268 122 A 143 143 0 1 0 473 122"
            fill="none" stroke="var(--icon-glow)" stroke-width="58" stroke-linecap="round"/>
      <line x1="371" y1="68" x2="371" y2="160"
            stroke="var(--icon-glow)" stroke-width="58" stroke-linecap="round"/>
    </svg>

    <ul class="contact">
      <li class="contact__email">quietharborretreats@mailverra.com</li>
      <li class="contact__social">www.friendspace.com/quietharborretreats</li>
      <li class="contact__events">www.quietharborretreats.ticketnest.com</li>
    </ul>
  </section>

</main>
</body>
</html>
```